Brightvale Minds Hub Brochure Design (Competition)

Create a compelling brochure design that stands out from other training and certification offerings in the training space and develop the final brochure with copy provided by the client. Our offering includes a technical component – BMH Nexa – which is a virtual ecosystem / online portal with robust capabilities for virtual events, etc. It is our unique value proposition. It’s how we’ll stand out in the marketplace. You’ll find this in the brochure map. But, the offering is first a training and certification value proposition. This is a new product offering.
The BMH Nexa portal will be a 3-D environment, which is leading edge in our space and very sophisticated looking. We need a contemporary style that reflects that forward leaning sophistication and works with the images provided. Suggest interconnectivity everywhere without always being explicit about interconnectivity.
The designer’s skills need to fall to the artistic side of the continuum rather to the layout designer side of the continuum. We want creativity; of course, the designer needs to be able to use the tools to turn the design into a brochure.
The brochure map is crafted around a 6-page brochure with cover, back, and fold out to reveal a spread. Unfortunately, it is copy heavy. I’ll continue to look for areas to thin it, but work with what you have giving air wherever you can.
The thinking behind the flow is as follows:
When the brochure is handed to someone, they will see the cover first. Then, typically, they will turn it over to look at the back. With that behavior in mind, the cover sets the stage for why people need BMH and the back cover identifies the ways people can partner with BMH. The inside spread offers the specifics. Also, if the reader opens the first fold and keeps the second fold closed, and then turns it over, the Why Partner and Why BMH are next to each other. When you craft the .pdf version, try to keep these connections in mind as you flow the pages.
We are open to an 8-page format. It will primarily be distributed as a .pdf file attached to email and/or downloaded from the website. We will print brochures for trade shows and proposal inserts, for example, and we want to keep print costs reasonable. This version of the brochure will not be used for direct mail; so, no address block is needed.
For the .pdf used for the website/email attachment, please sequence the pages: Cover – Inside left 2 – Inside center 3 – inside right page 4 – inside fold-in opposite in the inside left p5 – back page 6.
For the .pdf used for print, please sequence the pages so they support the 6-page fold in approach, if that is the design you propose. If the brochure map does not make that clear to you, please ask.
We have an existing logo and images that represent various areas in the online portal, attached. Note, we will have one more image for the online portal that will represent a virtual expo hall. Please use a placeholder image so we don’t forget to include it where appropriate.
CMYK colors
Cyan 99
Magenta 77
Yellow 4
Black 0.5
RGB Colors
Red 2
Green 79
Blue 159
CMYK colors
Cyan 57
Magenta 49
Yellow 48
Black 15
RGB Colors
Red 111
Green 111
Blue 111
Hello, designers. Everyone seems to be confused by the 6-page format. So, I've rewritten that instruction in the brochure map to help clarify. Also, I know that the brochure was copy heavy. Now that I see some designs, I have found several opportunities to cut copy and shorten some of the statements. Hopefully this will help everyone. Check the brief for the new brochure map, V3. Thank you all for playing.

```html
<!DOCTYPE html>
<html lang="en">
<head>
<meta charset="utf-8">
<title>BMH Nexa – Brochure Spread</title>
<link href="https://fonts.googleapis.com/css2?family=Exo+2:ital,wght@1,800&family=Ubuntu:wght@400;500;700&display=swap" rel="stylesheet">
<style>
  :root {
    --brand-blue: #024f9f;
    --brand-gray: #6f6f6f;
    --ink: #3b4150;
    --paper: #f7f8fb;
    --paper-shade: #eceef3;
    --backdrop: #2a2a2c;
  }
  * { box-sizing: border-box; margin: 0; padding: 0; }
  html, body {
    width: 1200px; height: 789px; overflow: hidden;
    background: var(--backdrop);
    font-family: "Ubuntu", sans-serif;
    color: var(--ink);
  }
  .spread {
    position: absolute; left: 77px; top: 24px;
    width: 1046px; height: 740px;
    display: flex;
  }
  .page {
    position: relative; width: 523px; height: 740px;
    background: var(--paper);
  }
  .page--left { background: linear-gradient(90deg, var(--paper) 88%, var(--paper-shade)); }
  .page--right { background: linear-gradient(90deg, var(--paper-shade), var(--paper) 12%); }

  .folio {
    position: absolute; top: 34px; font-size: 9px; color: var(--ink);
  }
  .folio::after {
    content: ""; position: absolute; top: -12px; width: 1px; height: 38px; background: var(--ink);
  }
  .page--left .folio { right: 26px; }
  .page--left .folio::after { right: -8px; }
  .page--right .folio { left: 26px; }
  .page--right .folio::after { left: -8px; }

  .page-title {
    position: absolute;
    font-family: "Exo 2", sans-serif; font-weight: 800; font-style: italic;
    color: var(--brand-blue); letter-spacing: 0.5px; text-transform: uppercase;
  }
  .page--left .page-title { left: 40px; top: 48px; font-size: 24px; }
  .page--right .page-title { left: 40px; top: 74px; font-size: 24px; }

  .intro {
    position: absolute; left: 40px; top: 100px; width: 440px;
    font-size: 10px; font-weight: 700; line-height: 1.35;
  }
  .intro p + p { margin-top: 6px; }

  .photo { position: absolute; border-radius: 1px; }
  .photo--lounge {
    background: linear-gradient(160deg, #cfd8e6 0%, #8d98ab 35%, #5a6273 65%, #3d4352 100%);
  }
  .photo--atrium {
    background: linear-gradient(180deg, #5a6478 0%, #9aa6b8 40%, #c7cfdb 70%, #8f99a9 100%);
  }
  .photo--hall {
    background: linear-gradient(170deg, #d9dde3 0%, #b7bfc9 40%, #9aa2ad 75%, #7d8591 100%);
  }

  .roles { position: absolute; font-size: 9.5px; line-height: 1.32; }
  .role + .role { margin-top: 10px; }
  .role-name, .zone-name {
    font-size: 9.5px; font-weight: 700; color: var(--brand-blue);
  }
  .role-name { text-transform: uppercase; }

  .zones { position: absolute; width: 232px; font-size: 9.5px; line-height: 1.32; }
  .zone { text-align: justify; }
  .zone + .zone { margin-top: 8px; }
</style>
</head>
<body>
<main class="spread">

  <section class="page page--left">
    <span class="folio">03</span>
    <h1 class="page-title">BMH Nexa</h1>
    <div class="intro">
      <p>A high-tech virtual ecosystem connecting all stakeholders in the career life-cycle</p>
      <p>A socially-engaging environment, BMH Nexa integrates career training, certification, the job marketplace, events, and creative resources in a single portal.</p>
    </div>
    <div class="photo photo--lounge" role="img" aria-label="Rendered virtual lounge with seating areas and visitors" style="left:30px; top:170px; width:470px; height:240px;"></div>

    <div class="roles" style="left:40px; top:430px; width:210px;">
      <div class="role">
        <h3 class="role-name">Learners</h3>
        <p>Review course offerings, register and attend classes, take exams, attend virtual events, and chat with other participants.</p>
      </div>
      <div class="role">
        <h3 class="role-name">Enterprise Buyers and Authorized Trainer Partners</h3>
        <p>Purchase and access all authorized training materials, publish your training schedule, register participants, host classes and webinars, and access course evaluations and test results for your learners and customers.</p>
      </div>
    </div>

    <div class="roles" style="left:272px; top:430px; width:220px;">
      <div class="role">
        <h3 class="role-name">Employers and Recruiters</h3>
        <p>Promote job vacancies, screen candidate resumes, schedule and conduct candidate interviews, and verify BMH credentials.</p>
      </div>
      <div class="role">
        <h3 class="role-name">Sponsors and Partners</h3>
        <p>Participate in the 24 X 365 virtual exhibit hall, chat with prospects, promote your products and services in banner ads, ticker tapes, virtual events and sponsored webcasts.</p>
      </div>
      <div class="role">
        <h3 class="role-name">Trainers</h3>
        <p>Purchase and access all authorized training materials, conduct online classes and take full advantage of BMH resources as a community member.</p>
      </div>
    </div>
  </section>

  <section class="page page--right">
    <span class="folio">04</span>
    <h2 class="page-title">Explore the Ecosystem</h2>

    <div class="zones" style="left:40px; top:114px;">
      <p class="zone"><span class="zone-name">The Lobby</span> - Visitors and registered members enter the ecosystem through a virtual lounge, then easily navigate throughout the space and network with others.</p>
      <p class="zone"><span class="zone-name">Networking Zone</span> - A hub of activity. Chat informally with colleagues, trainers, recruiters, and special guests. Participate in scheduled group discussions with topic experts and collect points on the leader board.</p>
      <p class="zone"><span class="zone-name">Learning Zone</span> - The training venue. Participants access the theatre and classrooms for live event experiences. Integrated with the LMS, training providers securely maintain student records, learning paths, progress and customer reports.</p>
    </div>
    <div class="photo photo--lounge" role="img" aria-label="Rendered virtual lobby with lounge seating" style="left:290px; top:120px; width:205px; height:150px;"></div>

    <div class="photo photo--atrium" role="img" aria-label="Rendered atrium with central reception desk" style="left:30px; top:340px; width:220px; height:150px;"></div>
    <div class="zones" style="left:265px; top:340px; width:230px;">
      <p class="zone"><span class="zone-name">Expo Zone</span> - A virtual trade show. Where sponsors and partners market their products and services 24 X 365 or on a scheduled event basis.</p>
      <p class="zone"><span class="zone-name">Idea Zone</span> - An online library and resource center. Site visitors can read blogs and articles, view videos on-demand, and access other free content, easily downloadable from the portal.</p>
      <p class="zone"><span class="zone-name">Gaming Zone</span> - The game center. Where visitors and community members play educational games, earn participation points and badges, watch the leader board, and keep track of activities.</p>
    </div>

    <div class="zones" style="left:40px; top:515px; width:215px;">
      <p class="zone"><span class="zone-name">Certification Zone</span> - The skills validation center. Where certification candidates register for and take proctored certification exams through a BMH authorized testing center.</p>
      <p class="zone"><span class="zone-name">Job Connect Zone</span> - A recruiting center. Where recruiters, companies and job seekers meet. This zone hosts job fairs complete with private interviewing rooms.</p>
      <p class="zone"><span class="zone-name">The Trainer's Hub</span> - Have private chats with trainers and special guests available during and after "office hours". Includes a private zone for authorized trainers to chat and share ideas with colleagues.</p>
    </div>
    <div class="photo photo--hall" role="img" aria-label="Rendered open hall with tables and visitors" style="left:270px; top:548px; width:225px; height:165px;"></div>
  </section>

</main>
</body>
</html>
```